Vale Insurance Agency - Business Cards

Hello, I am needing new trendy business cards for our Insurance Agency now that I have a new Logo. I have attached our new logo with several color options along with a business card design that I like. I am leaning towards burgundy and blue colors. I have attached our current business card. I have also attached a headshot of our company president, Dennis Holt, that you can use if you wish. Thank you so much in advance for all the wonderful designs!!!!

Target Market(s)

We want to look very professional to potential customers and we also want to look very professional so insurance companies will want to contract with us to sell their product.

Industry/Entity Type

Insurance

Contact Information for Business Card

Dennis Holt
dholt@valeinsgroup.com
Business: 660-555-0142
Fax: 660-555-0187
Cell: 660-555-0163
Toll Free: 888-555-0119
42 W Elm St Butler, MO 64730
www.valeinsgroup.net

Font styles to use
Serif
Sans Serif

Colors
0355a3
3277b5
f04a50
ec1f27

Requirements
Nice to have
• I love creativity. The more creative and balanced a business card design the more I will like it. I would like the card to be printed horizontally instead of vertically.
Should not have
• My project should not have the Allied Coverage Broker logo. It is no longer used in the industry.

```html
<!DOCTYPE html>
<html lang="en">
<head>
<meta charset="utf-8">
<title>Vale Insurance Agency – Business Cards</title>
<link href="https://fonts.googleapis.com/css2?family=Montserrat:wght@500;600;700&family=Open+Sans:wght@400;600&display=swap" rel="stylesheet">
<style>
  :root{
    --navy:#0b3a6e;
    --blue:#0355a3;
    --blue-light:#3277b5;
    --grey:#5a5a5a;
    --grey-dark:#3f3f3f;
    --white:#ffffff;
    --page:#e9eaec;
    --photo-a:#9a8f85;
    --photo-b:#4b4540;
  }
  *{box-sizing:border-box;margin:0;padding:0}
  html,body{width:1200px;height:899px;overflow:hidden;background:var(--page)}
  body{position:relative;font-family:"Open Sans",Arial,sans-serif}
  .card{position:absolute;width:540px;height:310px;border-radius:22px;overflow:hidden;box-shadow:0 10px 28px rgba(0,0,0,.18)}
  .card--front{left:40px;top:295px;background:linear-gradient(135deg,var(--navy) 0%,var(--blue) 60%,var(--blue-light) 100%)}
  .card--back{left:620px;top:295px;background:var(--white)}

  .brand{position:absolute;display:flex;align-items:center;gap:12px}
  .brand__dot{width:44px;height:44px;border-radius:50%;border:4px solid currentColor}
  .brand__rule{width:1.5px;height:48px;background:currentColor}
  .brand__name{font-family:"Montserrat",Arial,sans-serif;font-weight:600;font-size:17px;line-height:1.15;letter-spacing:.3px}
  .brand__name span{display:block;font-size:11px;letter-spacing:3px;text-align:center}
  .card--front .brand{left:270px;top:130px;color:var(--white)}
  .card--back .brand{left:250px;top:38px;color:var(--navy)}
  .card--back .brand__dot{color:var(--grey)}

  .band{position:absolute;left:0;right:0;top:145px;height:118px;background:linear-gradient(90deg,var(--navy),var(--blue))}
  .band__line{position:absolute;left:0;right:0;top:263px;height:6px;background:var(--white)}
  .footer{position:absolute;left:0;right:0;top:269px;bottom:0;background:linear-gradient(90deg,var(--grey-dark),var(--grey));color:var(--white);font-size:14px;display:flex;align-items:center;justify-content:center;letter-spacing:.3px;white-space:nowrap}

  .portrait{position:absolute;left:58px;top:32px;width:150px;height:146px;background:var(--white);border:2px solid var(--navy);padding:8px}
  .portrait__fill{width:100%;height:100%;background:radial-gradient(circle at 50% 40%,var(--photo-a),var(--photo-b))}

  .person{position:absolute;left:40px;width:186px;top:186px;text-align:center;color:var(--white)}
  .person__name{font-family:"Montserrat",Arial,sans-serif;font-weight:700;font-size:24px;white-space:nowrap}
  .person__title{font-size:12px;margin-top:1px}

  .contact{position:absolute;left:292px;top:160px;padding-left:16px;border-left:1.5px solid rgba(255,255,255,.7);color:var(--white);font-size:13.5px;line-height:21px;list-style:none;white-space:nowrap}
  .contact li{display:flex;align-items:center;gap:8px}
  .contact svg{width:12px;height:12px;flex:none}
</style>
</head>
<body>
  <section class="card card--front" aria-label="Card front">
    <div class="brand">
      <div class="brand__dot"></div>
      <div class="brand__rule"></div>
      <div class="brand__name">VALE INSURANCE<span>AGENCY INC</span></div>
    </div>
  </section>

  <section class="card card--back" aria-label="Card back">
    <div class="band"></div>
    <div class="band__line"></div>

    <div class="brand">
      <div class="brand__dot"></div>
      <div class="brand__rule"></div>
      <div class="brand__name">VALE INSURANCE<span>AGENCY INC</span></div>
    </div>

    <div class="portrait"><div class="portrait__fill" role="img" aria-label="Headshot of Dennis Holt"></div></div>

    <div class="person">
      <div class="person__name">Dennis Holt</div>
      <div class="person__title">Managing Director</div>
    </div>

    <ul class="contact">
      <li><svg viewBox="0 0 24 24" fill="#fff"><path d="M6.6 10.8a15 15 0 0 0 6.6 6.6l2.2-2.2c.3-.3.7-.4 1-.2 1.1.4 2.3.6 3.6.6.6 0 1 .4 1 1V20c0 .6-.4 1-1 1A17 17 0 0 1 3 4c0-.6.4-1 1-1h3.5c.6 0 1 .4 1 1 0 1.3.2 2.5.6 3.6.1.3 0 .7-.2 1z"/></svg>660-555-0142</li>
      <li><svg viewBox="0 0 24 24" fill="none" stroke="#fff" stroke-width="2.2"><rect x="6" y="2" width="12" height="20" rx="2"/><line x1="11" y1="18" x2="13" y2="18"/></svg>660-555-0163</li>
      <li><svg viewBox="0 0 24 24" fill="#fff"><path d="M2 5h20v14H2z"/><path d="M2 5l10 8 10-8" stroke="#0355a3" stroke-width="2" fill="none"/></svg>dholt@valeinsgroup.com</li>
      <li><svg viewBox="0 0 24 24" fill="none" stroke="#fff" stroke-width="2"><circle cx="12" cy="12" r="10"/><path d="M2 12h20M12 2c3 3 3 17 0 20M12 2c-3 3-3 17 0 20"/></svg>www.valeinsgroup.net</li>
    </ul>

    <div class="footer">42 W Elm St | P.O. Box 240 | Alder Falls, MO 64799</div>
  </section>
</body>
</html>
```